HollowPine Ventures Inc. Business Card Design

My business is custom renovations and homes.I would need to have a new business logo created to go along with my company name. The business card should be of a modern style as this is the market I am focused on. I would need my contact information and website posted on the card. I would also like to list a few of the tasks I conduct on the card (such as: Renovations, Additions, Repairs, New Homes, Design, Consultations). On the reverse of the card I currently have just my logo and my motto, "Shaping A Bold Path". However, I am open to completely changing everything as I am starting a new year and would like to excel further. Any new ideas and suggestions are always welcomed. Thank you.

Target Market(s)

Upscale residential and commercial renovations and builds

Industry/Entity Type

Business

Contact Information for Business Card

I would like the design to be able to be laser cut or burnt onto a wooden business card. I will be creating one option of cards for really loyal customers (wooden) and a second option for the everyday customer (paper).

Font styles to use
Other font styles liked:
• Calibri / anything of mordern taste

Colors
f37122
5c5c5c
474747
ffffff

Requirements
Must have
• I would like the colours of my business to be a sharp orange and grey. I believe this will symbolize a modern style. I am open to other suggestions if this is not suitable for the designers tastes. My contact info as follows:
• Will Marsh
• President
• HollowPine Ventures Inc.
• 555-214-3987
• will@hollowpineventures.example
• I would like my website (currently under construction) hollowpineventures.example on the card aswell.
Nice to have
• Along with a modern logo representing HollowPine, I would like something on the card besides the logo and contact information. Perhaps a small background design. I feel it may be nice to have my services listed on the card (in smaller font on the bottom) Renovations, Additions, Repairs, Design, Consultations.
Should not have
• The business card should not have too many different colors. Should not have rounded corners.

```html
<!DOCTYPE html>
<html lang="en">
<head>
<meta charset="utf-8">
<title>HollowPine Ventures Inc. Business Card</title>
<link href="https://fonts.googleapis.com/css2?family=Lato:wght@400;700&family=Roboto:wght@400&family=Ubuntu:wght@500;700&family=Open+Sans:wght@700&family=Yellowtail&display=swap" rel="stylesheet">
<style>
  :root {
    --orange: #f37122;
    --grey: #5c5c5c;
    --charcoal: #474747;
    --white: #ffffff;
    --ink: #111111;
    --backdrop: #e4e1dc;
  }
  * { margin: 0; padding: 0; box-sizing: border-box; }
  html, body { width: 1000px; height: 1200px; overflow: hidden; }
  body { background: var(--backdrop); position: relative; }

  .card {
    position: absolute;
    left: 84px;
    width: 832px;
    box-shadow: 0 4px 14px rgba(0,0,0,0.25);
  }
  .card--front { top: 92px; height: 485px; background: var(--white); }
  .card--back { top: 628px; height: 489px; background: var(--charcoal); }

  .brand {
    position: absolute;
    text-align: center;
    font-family: 'Lato', sans-serif;
    font-weight: 700;
  }
  .brand__name { font-size: 52px; line-height: 1; letter-spacing: 0.5px; }
  .brand__sub {
    display: flex; align-items: center; justify-content: center; gap: 10px;
    font-size: 19px; margin-top: 6px;
  }
  .brand__rule { display: block; width: 56px; height: 1px; background: currentColor; }

  .card--front .brand { left: 70px; width: 290px; top: 200px; color: var(--ink); }
  .card--back .brand { left: 266px; width: 300px; top: 238px; color: var(--white); }

  .divider {
    position: absolute; left: 399px; top: 186px;
    width: 1px; height: 112px; background: var(--grey);
  }

  .contact { position: absolute; left: 427px; top: 164px; }
  .contact__name {
    font-family: 'Ubuntu', sans-serif; font-weight: 700;
    font-size: 31px; color: var(--ink); line-height: 1.1; letter-spacing: 0.5px;
  }
  .contact__title {
    font-family: 'Ubuntu', sans-serif; font-weight: 700;
    font-size: 20px; color: var(--orange); margin-top: 2px;
  }
  .contact__list { list-style: none; margin-top: 12px; }
  .contact__item {
    display: flex; align-items: center; gap: 12px;
    font-family: 'Roboto', sans-serif; font-size: 20px; color: var(--ink);
    height: 27px;
  }
  .contact__icon { width: 16px; height: 16px; flex: none; }

  .motto {
    position: absolute; left: 0; width: 100%; top: 326px; text-align: center;
    font-family: 'Yellowtail', cursive; font-size: 32px; color: var(--white);
  }

  .services {
    position: absolute; left: 0; top: 425px; width: 100%; height: 39px;
    background: var(--white);
    display: flex; align-items: center; justify-content: center;
    font-family: 'Open Sans', sans-serif; font-weight: 700;
    font-size: 19.5px; color: var(--charcoal); letter-spacing: 0.1px;
    white-space: nowrap;
  }
</style>
</head>
<body>

<section class="card card--front">
  <div class="brand">
    <div class="brand__name">HollowPine</div>
    <div class="brand__sub"><span class="brand__rule"></span>Ventures Inc<span class="brand__rule"></span></div>
  </div>

  <div class="divider"></div>

  <div class="contact">
    <div class="contact__name">WILL MARSH</div>
    <div class="contact__title">PRESIDENT</div>
    <ul class="contact__list">
      <li class="contact__item">
        <svg class="contact__icon" viewBox="0 0 16 16" aria-hidden="true"><path fill="var(--orange)" d="M3.2 1.2l2.3 2.6-1.3 1.8c.9 2 2.4 3.5 4.3 4.4l1.8-1.3 2.6 2.3-1.4 2.3C6.6 13.3 2.7 9.4 1 4.6z"/></svg>
        555-214-3987
      </li>
      <li class="contact__item">
        <svg class="contact__icon" viewBox="0 0 16 16" aria-hidden="true"><rect x="1" y="3" width="14" height="10" fill="var(--orange)"/><path d="M1.5 3.5L8 9l6.5-5.5" fill="none" stroke="var(--white)" stroke-width="1.3"/></svg>
        will@hollowpineventures.example
      </li>
      <li class="contact__item">
        <svg class="contact__icon" viewBox="0 0 16 16" aria-hidden="true"><rect x="1.5" y="2.5" width="13" height="9" fill="none" stroke="var(--orange)" stroke-width="1.6"/><rect x="5" y="13" width="6" height="1.6" fill="var(--orange)"/></svg>
        hollowpineventures.example
      </li>
    </ul>
  </div>
</section>

<section class="card card--back">
  <div class="brand">
    <div class="brand__name">HollowPine</div>
    <div class="brand__sub"><span class="brand__rule"></span>Ventures Inc<span class="brand__rule"></span></div>
  </div>
  <div class="motto">Shaping A Bold Path</div>
  <div class="services">RENOVATIONS | ADDITIONS | REPAIRS | NEW HOMES | DESIGN | CONSULTATIONS</div>
</section>

</body>
</html>
```